Flyer for the Harvest of lanterns conference

Flyer design for an annual international conference called "MERIVAL 2017". This is a conference for young adults, so we hope to produce a design that is both professional and appealing to young people in general

We'd like the flyer to showcase the conference brand logo, and clearly highlight the key information to people who will read it.

Target Market(s)

Young people, young adults

Industry/Entity Type

Religious

Font styles to use
Sans Serif

Colors

Designer to choose colors to be used in the design.

Requirements
Must have
• - Should be only one page (Vertical or Horizontal).
• - the MERVAL logo and all the information found in the attached text file. This includes: Main topic: Your sons and daughters shall prophesy,
• Dates and time, location, contact information and everything that is in the attached text file.
Nice to have
• It would be nice to see samples where the white logo is used and another where the black one is used.
Should not have
• This is NOT a folded flyer, we will be sticking it on doors and public places. And we will be printing large simple to put on walls. So only one page with few words like an add (the words are in the attached file)

```html
<!DOCTYPE html>
<html lang="en">
<head>
<meta charset="utf-8">
<title>Harvest of Lanterns Conference – MERIVAL 2017</title>
<link rel="stylesheet" href="https://fonts.googleapis.com/css2?family=Bebas+Neue&family=Montserrat:wght@500;600;700&family=Open+Sans:wght@400;600;700&display=swap">
<style>
  :root {
    --backdrop: #e6e6e4;
    --paper: #ffffff;
    --ink: #222222;
    --badge: #2b2b2b;
    --yellow: #ffd200;
    --yellow-deep: #e2b800;
    --orange: #e57c0a;
    --orange-text: #f08a00;
    --bar: #111111;
  }
  * { box-sizing: border-box; margin: 0; padding: 0; }
  html, body { width: 1200px; height: 1200px; overflow: hidden; background: var(--backdrop); }
  .flyer {
    position: absolute; left: 180px; top: 15px; width: 840px; height: 1170px;
    background: var(--paper); overflow: hidden;
    font-family: "Montserrat", sans-serif; color: var(--ink);
  }
  .backdrop-photo {
    position: absolute; left: 0; top: 560px; width: 840px; height: 560px;
    background: linear-gradient(180deg, rgba(255,255,255,0) 0%, rgba(210,210,210,.35) 45%, rgba(200,200,200,.3) 100%);
  }
  .ribbon { position: absolute; top: 168px; height: 300px; width: 200px; }
  .ribbon--left { left: 12px; }
  .ribbon--right { right: 12px; }
  .badge { position: absolute; left: 148px; top: 32px; width: 544px; height: 544px; }
  .badge-name {
    position: absolute; left: 148px; width: 544px; text-align: center;
    font-family: "Bebas Neue", sans-serif; color: var(--yellow);
  }
  .badge-name--title { top: 150px; font-size: 128px; letter-spacing: 4px; line-height: 1; }
  .badge-name--year { top: 330px; font-size: 112px; line-height: 1; }
  .headline { position: absolute; left: 0; width: 840px; top: 612px; text-align: center; }
  .headline-top { font-weight: 600; font-size: 54px; letter-spacing: 1px; line-height: 1; }
  .headline-band {
    display: inline-block; margin-top: 10px; background: var(--ink); color: var(--yellow);
    font-weight: 600; font-size: 56px; padding: 8px 30px 10px; line-height: 1;
    box-shadow: 0 6px 0 rgba(0,0,0,.12);
  }
  .tagline { margin-top: 16px; font-weight: 700; font-size: 19px; letter-spacing: 1px; }
  .speakers { position: absolute; left: 0; top: 826px; width: 840px; height: 80px; display: flex; }
  .speakers-label {
    width: 172px; background: var(--yellow); display: flex; align-items: center; justify-content: center;
    font-family: "Bebas Neue", sans-serif; font-size: 36px; letter-spacing: 1px;
  }
  .speakers-list {
    flex: 1; background: var(--orange); color: #fff; display: grid;
    grid-template-columns: 1fr 0.8fr 1fr; align-content: center; padding: 0 18px; row-gap: 4px;
    font-family: "Open Sans", sans-serif; font-weight: 700; font-size: 13px; list-style: none;
  }
  .speakers-list li::before { content: "• "; }
  .schedule { position: absolute; left: 70px; top: 918px; font-family: "Bebas Neue", sans-serif; line-height: .95; }
  .schedule-days { color: var(--orange-text); font-size: 62px; }
  .schedule-month { color: var(--ink); font-size: 62px; }
  .start-time {
    position: absolute; left: 420px; top: 926px; width: 330px; height: 100px; background: var(--yellow);
    font-family: "Bebas Neue", sans-serif; font-size: 110px; line-height: 108px; text-align: center; color: var(--ink);
  }
  .hall {
    position: absolute; right: 42px; top: 1052px; display: flex; align-items: center; gap: 14px;
    font-family: "Open Sans", sans-serif; font-weight: 600; font-size: 25px;
  }
  .venue {
    position: absolute; left: 40px; top: 1044px; display: flex; align-items: center; gap: 14px;
    font-family: "Open Sans", sans-serif; font-style: normal; font-weight: 600; font-size: 15px; line-height: 1.15;
  }
  .contact-bar {
    position: absolute; left: 0; bottom: 0; width: 840px; height: 62px; background: var(--bar); color: #fff;
    display: flex; justify-content: space-around; align-items: center;
    font-family: "Open Sans", sans-serif; font-size: 19px;
  }
  .contact-bar span { display: flex; align-items: center; gap: 8px; }
</style>
</head>
<body>
<main class="flyer">
  <div class="backdrop-photo" role="img" aria-label="Faded black and white photo of young people worshipping"></div>

  <svg class="ribbon ribbon--left" viewBox="0 0 200 300" aria-hidden="true">
    <polygon points="0,0 60,0 60,300 0,280" fill="var(--yellow-deep)"/>
    <polygon points="60,0 200,0 200,300 60,300" fill="var(--yellow)"/>
  </svg>
  <svg class="ribbon ribbon--right" viewBox="0 0 200 300" aria-hidden="true">
    <polygon points="0,0 140,0 140,300 0,300" fill="var(--yellow)"/>
    <polygon points="140,0 200,15 200,290 140,300" fill="var(--yellow-deep)"/>
  </svg>

  <svg class="badge" viewBox="0 0 544 544" aria-hidden="true">
    <circle cx="272" cy="272" r="270" fill="#fff"/>
    <circle cx="272" cy="272" r="242" fill="var(--badge)" stroke="var(--badge)" stroke-width="6"/>
    <circle cx="272" cy="272" r="248" fill="none" stroke="#fff" stroke-width="3"/>
    <circle cx="272" cy="272" r="226" fill="none" stroke="#fff" stroke-width="6" stroke-dasharray="5 7"/>
  </svg>
  <div class="badge-name badge-name--title">MERVAL</div>
  <div class="badge-name badge-name--year">2017</div>

  <header class="headline">
    <h1 class="headline-top">HARVEST OF</h1>
    <div class="headline-band">LANTERNS CONFERENCE</div>
    <p class="tagline">YOUR SONS AND DAUGHTERS SHALL PROPHESY</p>
  </header>

  <section class="speakers">
    <div class="speakers-label">SPEAKERS</div>
    <ul class="speakers-list">
      <li>Prophet Marc Delorne</li>
      <li>Prophet Jonas Vireli</li>
      <li>Prophet Caleb Moran Tesfa</li>
      <li>Bishop Samuel Odeku</li>
      <li>Prophet Ruben Amsel</li>
    </ul>
  </section>

  <div class="schedule">
    <div class="schedule-days">1ST, 2ND AND 3RD</div>
    <div class="schedule-month">SEPTEMBER 2017</div>
  </div>
  <div class="start-time">6:00PM</div>

  <div class="hall">
    <svg width="30" height="30" viewBox="0 0 30 30" aria-hidden="true">
      <path d="M15 3 L28 15 H24 V27 H6 V15 H2 Z" fill="var(--orange)"/>
      <rect x="12" y="18" width="6" height="9" fill="#fff"/>
    </svg>
    Cedar Hall
  </div>

  <address class="venue">
    <svg width="32" height="44" viewBox="0 0 32 44" aria-hidden="true">
      <path d="M16 2 C8 2 3 8 3 15 C3 24 16 36 16 36 C16 36 29 24 29 15 C29 8 24 2 16 2 Z" fill="var(--orange)"/>
      <circle cx="16" cy="15" r="5" fill="#fff"/>
      <ellipse cx="16" cy="39" rx="12" ry="3.5" fill="none" stroke="#111" stroke-width="2.5"/>
    </svg>
    <span>Harborview Lantern Hotel<br>418 Elmcrest Avenue Lakeport,<br>ME 04920 United States</span>
  </address>

  <footer class="contact-bar">
    <span>
      <svg width="16" height="16" viewBox="0 0 16 16" aria-hidden="true"><path d="M3 1 L6 1 L7 5 L5 6 C6 8 8 10 10 11 L11 9 L15 10 L15 13 C15 14 14 15 13 15 C7 15 1 9 1 3 C1 2 2 1 3 1 Z" fill="#fff"/></svg>
      +1 (555) 014 2290
    </span>
    <span>
      <svg width="16" height="12" viewBox="0 0 16 12" aria-hidden="true"><rect x="0.5" y="0.5" width="15" height="11" fill="none" stroke="#fff"/><path d="M1 1 L8 7 L15 1" fill="none" stroke="#fff"/></svg>
      hello@lanternharvest.org
    </span>
    <span>
      <svg width="16" height="16" viewBox="0 0 16 16" aria-hidden="true"><circle cx="8" cy="8" r="7" fill="none" stroke="#fff" stroke-width="1.5"/><path d="M1 8 H15 M8 1 C4 5 4 11 8 15 M8 1 C12 5 12 11 8 15" fill="none" stroke="#fff"/></svg>
      http://meriva.org
    </span>
  </footer>
</main>
</body>
</html>
```